Business Card Design needed for start up company Pramora

In need of a new business card designed for a start up company based in Sydney, Pramora is a new start up innovative Company, our mission it to make property accessible for everyday Australian and to become the leading Real Estate platform in Australia. We want it to be fresh and clean.

Industry/Entity Type

Financial

Contact Information for Business Card

Section for Name
Section for Title

PRAMORA - Where Doors Open Wide
Mobile:
Direct:

Font styles to use
Sans Serif

Colors
33a6d7
0692cd
0255a3
ffffff

Requirements
Must have
• Logo, all business card details

```html
<!DOCTYPE html>
<html lang="en">
<head>
<meta charset="UTF-8">
<title>Pramora Business Card</title>
<link rel="stylesheet" href="https://fonts.googleapis.com/css2?family=Montserrat:wght@500;600;800&family=Roboto:wght@400&display=swap">
<style>
  :root {
    --bg: #e6e6e6;
    --card: #ffffff;
    --sky: #56c0ee;
    --sky-deep: #33a6d7;
    --navy: #2446a0;
  }
  * { margin: 0; padding: 0; box-sizing: border-box; }
  html, body { width: 1200px; height: 900px; overflow: hidden; background: var(--bg); }
  .canvas { position: relative; width: 1200px; height: 900px; }

  .card {
    position: absolute;
    width: 560px;
    height: 320px;
    border-radius: 26px;
    background: var(--card);
    overflow: hidden;
    box-shadow: 0 6px 16px rgba(0,0,0,0.12);
  }
  .card--front { left: 150px; top: 90px; }
  .card--back  { left: 490px; top: 490px; }

  .dot-field {
    position: absolute;
    inset: 0;
    background:
      radial-gradient(ellipse 62% 56% at 50% 50%, var(--card) 0%, var(--card) 62%, rgba(255,255,255,0) 92%),
      linear-gradient(135deg, var(--sky) 0%, var(--sky-deep) 45%, var(--navy) 100%);
  }

  .brand {
    position: absolute;
    left: 50%; top: 50%;
    transform: translate(-50%, -50%);
    display: flex;
    flex-direction: column;
    align-items: center;
    gap: 10px;
  }
  .brand__row { display: flex; align-items: center; gap: 14px; }
  .brand__mark {
    width: 52px; height: 52px;
    border-radius: 50%;
    background: var(--sky);
  }
  .brand__name {
    font-family: "Montserrat", sans-serif;
    font-weight: 800;
    font-size: 48px;
    letter-spacing: 1px;
    color: var(--navy);
  }
  .brand__tagline {
    font-family: "Montserrat", sans-serif;
    font-weight: 500;
    font-size: 12px;
    letter-spacing: 3px;
    color: var(--sky-deep);
    white-space: nowrap;
  }

  .identity {
    position: absolute;
    left: 50%; top: 50%;
    transform: translate(-50%, -50%);
    display: flex;
    align-items: center;
    gap: 22px;
  }
  .identity__person { display: flex; flex-direction: column; gap: 6px; }
  .identity__name {
    font-family: "Montserrat", sans-serif;
    font-weight: 600;
    font-size: 24px;
    letter-spacing: 2px;
    color: var(--navy);
    white-space: nowrap;
  }
  .identity__title {
    font-family: "Roboto", sans-serif;
    font-size: 11px;
    letter-spacing: 2px;
    color: var(--sky-deep);
    white-space: nowrap;
  }
  .identity__divider {
    width: 1px; height: 56px;
    background: var(--sky);
  }
  .contact { list-style: none; }
  .contact__item {
    display: flex;
    align-items: center;
    gap: 8px;
    font-family: "Roboto", sans-serif;
    font-size: 12px;
    letter-spacing: 1px;
    line-height: 18px;
    color: var(--sky-deep);
    white-space: nowrap;
  }
  .contact__icon { width: 11px; height: 11px; flex: none; }
</style>
</head>
<body>
<main class="canvas">

  <section class="card card--front">
    <div class="dot-field" role="img" aria-label="Scattered light and dark blue dot pattern around the card edges"></div>
    <div class="brand">
      <div class="brand__row">
        <span class="brand__mark"></span>
        <span class="brand__name">PRAMORA</span>
      </div>
      <p class="brand__tagline">WHERE DOORS OPEN WIDE</p>
    </div>
  </section>

  <section class="card card--back">
    <div class="dot-field" role="img" aria-label="Scattered light and dark blue dot pattern around the card edges"></div>
    <div class="identity">
      <div class="identity__person">
        <h1 class="identity__name">JOHN DOE</h1>
        <p class="identity__title">PROPERTY ADVISOR</p>
      </div>
      <span class="identity__divider"></span>
      <ul class="contact">
        <li class="contact__item">
          <svg class="contact__icon" viewBox="0 0 12 12"><path d="M2.5 1 L4.5 1 L5 3.5 L3.8 4.5 C4.5 6 6 7.5 7.5 8.2 L8.5 7 L11 7.5 L11 9.5 C11 10.3 10.3 11 9.5 11 C5 11 1 7 1 2.5 C1 1.7 1.7 1 2.5 1 Z" fill="var(--navy)"/></svg>
          M: 0412 648 390
        </li>
        <li class="contact__item">
          <svg class="contact__icon" viewBox="0 0 12 12"><path d="M2.5 1 L4.5 1 L5 3.5 L3.8 4.5 C4.5 6 6 7.5 7.5 8.2 L8.5 7 L11 7.5 L11 9.5 C11 10.3 10.3 11 9.5 11 C5 11 1 7 1 2.5 C1 1.7 1.7 1 2.5 1 Z" fill="var(--navy)"/></svg>
          D: +61 2 8047 1523
        </li>
        <li class="contact__item">
          <svg class="contact__icon" viewBox="0 0 12 12"><rect x="1" y="2.5" width="10" height="7" fill="none" stroke="var(--navy)" stroke-width="1.2"/><path d="M1 2.5 L6 6.5 L11 2.5" fill="none" stroke="var(--navy)" stroke-width="1.2"/></svg>
          john@pramora.au
        </li>
      </ul>
    </div>
  </section>

</main>
</body>
</html>
```